Design Tweak needed for a current site

Design on top of an existing quiz funnel

Ideally we would like to tweak what we have already built here (moving elements, styles, adding simple elements etc): http://offers.plumrivetdeals.com/can-you-save-on-car-insurance

The flow:
1) User lands on the quiz page
2) User answers X questions and moves through the flow
3) Calculating user results screen
4) User reaches a success screen, and is subsequently redirected

Keys to the design:
1) We need to emphasize the quiz title as that will drive engagement. In this case, this is a quiz to see if you might be eligible to save money on car insurance.

2) At the end of the quiz we need to make it very, very clear that the user is eligible for savings and that in order to complete the process they are being redirected to another page where they need to fill out a form. It is critical that the design communicates this very clearly... We can count down the time left until redirect and we can use any order of elements to make this point. I think our current design does a very bad job of this.

3) We want to have a "calculating" step so that it seems like the page is working in the background

Goals of the design:
1) Polished, high quality experience throughout
2) User is clearly prepared to be redirected to the conversion funnel/landing page at the end
3) User understands the value of completing the quiz

Target Market(s)

designers

Industry/Entity Type

Moving

Number of Pages Required

1 page

Font styles to use
Sans Serif

Colors

Designer to choose colors to be used in the design.

Requirements
Must have
• This quiz funnel is a template so while the current use case is for auto insurance, we would like a design that also would work in other contexts.
Should not have
• We don't want to materially change the core functionality of the quiz itself... redesigning any of the elements or interactions is encouraged though

```html
<!DOCTYPE html>
<html lang="en">
<head>
<meta charset="UTF-8">
<title>PlumRivet – Are You Overpaying for Car Insurance?</title>
<link rel="stylesheet" href="https://fonts.googleapis.com/css2?family=Roboto:ital,wght@0,400;0,500;0,700;1,400;1,500&display=swap">
<style>
  :root {
    --brand-blue: #0066ff;
    --brand-yellow: #ffcc00;
    --white: #ffffff;
    --option-grey: #e2e2e2;
    --ink: #111111;
    --dot-idle: #ffffff;
  }
  * { box-sizing: border-box; margin: 0; padding: 0; }
  html, body { width: 1200px; height: 667px; overflow: hidden; }
  body {
    background: var(--brand-blue);
    font-family: "Roboto", Arial, sans-serif;
    color: var(--white);
    position: relative;
  }
  .brand {
    position: absolute; left: 113px; top: 36px;
    display: flex; align-items: center; gap: 9px;
  }
  .brand-dot {
    width: 27px; height: 27px; border-radius: 50%;
    background: var(--white);
  }
  .brand-name {
    font-size: 27px; font-weight: 500; color: var(--white);
    letter-spacing: -0.2px;
  }
  .intro {
    position: absolute; left: 98px; top: 200px; width: 360px;
    text-align: center;
  }
  .intro-kicker {
    font-size: 54px; font-weight: 700; color: var(--brand-yellow);
    line-height: 1; letter-spacing: 0.5px;
  }
  .intro-title {
    margin-top: 22px;
    font-size: 31px; font-weight: 700; line-height: 36px;
    text-transform: uppercase;
  }
  .intro-text {
    margin-top: 34px;
    font-size: 16px; font-style: italic; line-height: 21px;
    text-transform: uppercase;
  }
  .quiz-backing {
    position: absolute; left: 537px; top: 102px;
    width: 554px; height: 540px;
    background: var(--white); border-radius: 4px;
  }
  .quiz-card {
    position: absolute; left: 521px; top: 87px;
    width: 556px; height: 541px;
    background: var(--brand-yellow); border-radius: 4px;
  }
  .quiz-step {
    position: absolute; top: 18px; left: 0; right: 0;
    text-align: center; font-size: 18px; font-weight: 700;
  }
  .quiz-question {
    position: absolute; left: 62px; top: 110px;
    display: flex; align-items: center; gap: 30px;
    font-size: 24px; font-style: italic; text-transform: uppercase;
  }
  .quiz-question svg { width: 20px; height: 22px; }
  .quiz-options {
    position: absolute; left: 62px; top: 218px;
    display: flex; gap: 62px;
  }
  .option {
    width: 185px; height: 184px;
    background: var(--option-grey); border-radius: 6px;
    display: flex; flex-direction: column; align-items: center;
    color: var(--ink);
  }
  .option svg { margin-top: 26px; width: 90px; height: 82px; }
  .option-label {
    margin-top: 20px;
    font-size: 22px; font-weight: 700; text-transform: uppercase;
  }
  .quiz-progress {
    position: absolute; top: 470px; left: 0; right: 0;
    display: flex; justify-content: center; gap: 20px;
  }
  .progress-dot {
    width: 9px; height: 9px; border-radius: 50%;
    background: var(--dot-idle);
  }
  .progress-dot.is-current { background: var(--brand-blue); }
</style>
</head>
<body>
  <header class="brand">
    <span class="brand-dot"></span>
    <span class="brand-name">PlumRivet</span>
  </header>

  <section class="intro">
    <p class="intro-kicker">QUIZ:</p>
    <h1 class="intro-title">Are you overpaying<br>for car insurance?</h1>
    <p class="intro-text">Take our five question quiz<br>to see if you might be eligible for<br>car insurance savings</p>
  </section>

  <div class="quiz-backing"></div>
  <section class="quiz-card">
    <p class="quiz-step">QUESTION 1/5</p>
    <div class="quiz-question">
      <svg viewBox="0 0 20 22"><polygon points="0,0 20,11 0,22" fill="var(--brand-blue)"/></svg>
      <span>Do you lease or own?</span>
    </div>
    <div class="quiz-options">
      <div class="option">
        <svg viewBox="0 0 90 82" fill="none" stroke="#111" stroke-width="4">
          <path d="M16 2 H50 L64 16 V64 H16 Z" stroke-linejoin="round"/>
          <path d="M50 2 V16 H64"/>
          <line x1="26" y1="22" x2="42" y2="22"/>
          <line x1="26" y1="32" x2="54" y2="32"/>
          <line x1="26" y1="42" x2="44" y2="42"/>
          <line x1="26" y1="52" x2="38" y2="52"/>
          <circle cx="62" cy="60" r="19" fill="var(--option-grey)"/>
          <path d="M52 64 V58 L56 52 H68 L72 58 V64 Z" fill="#111" stroke-width="1"/>
          <rect x="59" y="48" width="6" height="4" fill="#111" stroke="none"/>
        </svg>
        <span class="option-label">I lease!</span>
      </div>
      <div class="option">
        <svg viewBox="0 0 90 82" fill="none" stroke="#111" stroke-width="4" stroke-linejoin="round">
          <path d="M4 58 V40 L14 30 L24 14 H40 V58 Z"/>
          <line x1="46" y1="6" x2="46" y2="66"/>
          <rect x="10" y="42" width="10" height="7" rx="2"/>
          <line x1="12" y1="58" x2="12" y2="68"/>
          <line x1="34" y1="58" x2="34" y2="68"/>
          <circle cx="70" cy="38" r="16"/>
          <text x="70" y="45" text-anchor="middle" font-family="Roboto, Arial, sans-serif" font-size="20" font-weight="700" fill="#111" stroke="none">$</text>
        </svg>
        <span class="option-label">I own!</span>
      </div>
    </div>
    <div class="quiz-progress">
      <span class="progress-dot is-current"></span>
      <span class="progress-dot"></span>
      <span class="progress-dot"></span>
      <span class="progress-dot"></span>
      <span class="progress-dot"></span>
    </div>
  </section>
</body>
</html>
```